web site update

I want to get a better website for a small high end remodeling and construction company
I currently have a web site but you will find that it is not good.
www.quenbrickhall.com
We are a high end construction / remodeling company that has been in business since 2003. We primarily work in the mid peninsula of the bay area. Most of our clientele are very educated captains of industry. This group is still the target client.
I had my logo designed by Mint Easel a few years ago and I do like it, I like the orange and black or orange a blue. I don’t have a lot of content on hand as far as professional photographs.
Number of pages not sure and are open to: design pages vs full function website
I think what I am after is a web presence that will seal the deal as we are getting high referrals from past clients.
Construction
1 page

```html
<!DOCTYPE html>
<html lang="en">
<head>
<meta charset="utf-8">
<title>Quen Brickhall Remodeling</title>
<link href="https://fonts.googleapis.com/css2?family=Open+Sans:ital,wght@0,400;0,600;0,700;1,400&display=swap" rel="stylesheet">
<style>
:root{
  --orange:#ff6a00;
  --ink:#111111;
  --black:#000000;
  --text:#555555;
  --light:#f5f5f5;
  --footer:#121210;
  --muted:#8a8a8a;
  --white:#ffffff;
}
*{margin:0;padding:0;box-sizing:border-box}
html,body{width:702px;height:1200px;overflow:hidden;background:var(--white)}
body{font-family:"Open Sans",Arial,sans-serif;color:var(--ink);position:relative}
.section{position:absolute;left:0;width:702px}
.abs{position:absolute}

/* header */
.site-header{top:0;height:50px;border-top:2px solid var(--orange);background:var(--white);z-index:2}
.brand-bump{left:70px;top:20px;width:88px;height:52px;border-radius:0 0 44px 44px;background:var(--white)}
.brand{left:84px;top:10px;display:flex;align-items:center;gap:7px}
.brand-mark{width:28px;height:28px;background:var(--orange)}
.brand-name{font-weight:700;font-size:11px;line-height:13px;color:var(--ink);letter-spacing:.3px}
.main-nav{left:325px;top:20px;display:flex;gap:0}
.main-nav a{font-size:7px;font-weight:600;color:var(--ink);text-decoration:none;letter-spacing:.2px}
.nav-home{position:absolute;left:0;color:var(--orange)!important}
.nav-about{position:absolute;left:48px}
.nav-contact{position:absolute;left:96px;white-space:nowrap}
.nav-gallery{position:absolute;left:165px}
.call{left:536px;top:16px;display:flex;align-items:center;gap:6px}
.call-icon{width:18px;height:18px;border-radius:50%;background:var(--orange);display:flex;align-items:center;justify-content:center}
.call-text{font-size:8px;line-height:11px;color:#333}

/* hero */
.hero{top:50px;height:304px;background:linear-gradient(120deg,#6d6a63 0%,#8c877d 35%,#b7b1a4 60%,#7b766e 100%)}
.hero-frame{left:94px;top:54px;width:287px;height:196px;border:5px solid var(--orange);background:rgba(40,40,40,.72);transform:skewY(-2deg)}
.hero-copy{left:116px;top:112px;width:240px;color:var(--white)}
.hero-title{font-size:20px;font-weight:700;letter-spacing:.3px}
.hero-sub{font-size:11px;font-weight:600;margin-top:5px;letter-spacing:.2px}
.hero-text{font-size:7px;line-height:10.5px;margin-top:9px}
.hero-dots{left:117px;top:212px;display:flex;gap:2px}
.hero-dots span{width:7px;height:7px;border-radius:50%;background:var(--white)}
.hero-dots span.on{background:var(--orange)}
.arrow{top:136px}

/* features */
.features{top:354px;height:112px;background:var(--black)}
.feature{top:22px;width:150px}
.feature h3{position:absolute;left:50px;top:0;font-size:9.5px;font-weight:600;color:var(--white);white-space:nowrap}
.feature p{position:absolute;left:48px;top:20px;width:110px;font-size:5.6px;line-height:10.5px;color:#cfcfcf}
.feature .more{position:absolute;left:48px;top:62px;font-size:6px;font-weight:700;color:var(--orange);white-space:nowrap}
.feature svg{position:absolute;left:0;top:0}

/* gallery */
.gallery{top:466px;height:232px;background:var(--white)}
.section-title{font-size:12.5px;font-weight:700;color:var(--ink);letter-spacing:.2px}
.section-title em{font-style:normal;color:var(--orange)}
.gallery .section-title{left:0;width:702px;top:15px;text-align:center}
.filters{left:0;width:702px;top:41px;display:flex;justify-content:center;gap:14px;font-size:6.6px;color:#333}
.filters .active{color:var(--orange)}
.thumb{top:64px;width:122px;height:123px;border:2px solid #e6e6e6}
.dots{left:0;width:702px;top:210px;display:flex;justify-content:center;gap:3px}
.dots span{width:6px;height:6px;border-radius:50%;background:#777}
.dots span.on{background:var(--black)}

/* about */
.about{top:698px;height:196px;background:var(--light);border-top:1px solid #e8e8e8;border-bottom:1px solid #e8e8e8}
.about-title{left:94px;top:28px;font-size:12.5px;line-height:18px;font-weight:700}
.about-title span{color:var(--orange);display:block}
.about-text{left:94px;top:70px;width:205px;font-size:5.8px;line-height:11px;color:var(--text)}
.btn{left:94px;top:144px;width:67px;height:22px;background:var(--orange);color:var(--white);font-size:6.4px;font-weight:700;display:flex;align-items:center;justify-content:center;gap:4px;border-radius:2px}
.about-photo{top:30px;width:142px;height:136px}

/* testimonials */
.testimonials{top:894px;height:134px;background:var(--white)}
.testimonials .section-title{left:94px;top:22px}
.avatar{left:94px;top:48px;width:68px;height:68px;border-radius:50%;background:linear-gradient(160deg,#cfd6df,#8a94a3)}
.quote-badge{left:139px;top:91px;width:23px;height:23px;border-radius:50%;background:var(--orange);color:var(--white);font-size:15px;font-weight:700;display:flex;align-items:center;justify-content:center;line-height:1}
.quote{left:174px;top:52px;width:436px;font-size:6.4px;line-height:10.6px;font-style:italic;color:#444}
.quote b{color:var(--orange);font-style:normal}
.author{left:174px;top:103px;font-size:6px;color:#444}

/* footer */
.site-footer{top:1028px;height:138px;background:var(--footer)}
.footer-brand{left:88px;top:47px;display:flex;align-items:center;gap:6px}
.footer-brand .brand-mark{width:34px;height:34px;background:#6e6e6e}
.footer-brand .brand-name{color:#8f8f8f;font-size:10px;line-height:12px;font-weight:600}
.footer-head{top:28px;font-size:8.5px;font-weight:600;color:var(--white);letter-spacing:.2px}
.links{left:253px;top:49px;font-size:5.8px;line-height:12.2px;color:var(--white)}
.contact{left:354px;top:48px;font-size:5.8px;color:#bbb}
.contact .row{display:flex;gap:6px;margin-bottom:5px;line-height:9.5px}
.contact .ico{width:6px;color:var(--orange);flex:none}
.socials{left:354px;top:96px;display:flex;gap:3px}
.socials span{width:15px;height:15px;border-radius:50%;border:1px solid #999}
.field{left:503px;width:105px;height:14px;background:#2e2e2c;font-size:5.6px;font-style:italic;color:#aaa;padding:4px 4px}
.submit{left:503px;top:103px;width:44px;height:16px;background:var(--orange);color:var(--white);font-size:6.2px;font-weight:700;display:flex;align-items:center;justify-content:center}

/* bottom bar */
.bottom-bar{top:1166px;height:34px;background:var(--orange);color:var(--white);font-size:5.6px}
.legal{left:94px;top:14px}
.copyright{left:443px;top:14px}
.tag{left:635px;top:14px}
</style>
</head>
<body>

<header class="section site-header">
  <div class="abs brand-bump"></div>
  <div class="abs brand">
    <div class="brand-mark"></div>
    <div class="brand-name">QUEN BRICKHALL<br>REMODELING</div>
  </div>
  <nav class="abs main-nav">
    <a class="nav-home" href="#">HOME</a>
    <a class="nav-about" href="#">ABOUT</a>
    <a class="nav-contact" href="#">CONTACT US</a>
    <a class="nav-gallery" href="#">GALLERY</a>
  </nav>
  <div class="abs call">
    <div class="call-icon">
      <svg width="9" height="9" viewBox="0 0 24 24"><path fill="#fff" d="M6.6 10.8a15 15 0 0 0 6.6 6.6l2.2-2.2a1 1 0 0 1 1-.25 11.4 11.4 0 0 0 3.6.57 1 1 0 0 1 1 1V20a1 1 0 0 1-1 1A17 17 0 0 1 3 4a1 1 0 0 1 1-1h3.5a1 1 0 0 1 1 1c0 1.25.2 2.45.57 3.6a1 1 0 0 1-.25 1z"/></svg>
    </div>
    <div class="call-text">CALL US:<br>415.555.0142</div>
  </div>
</header>

<section class="section hero" role="img" aria-label="Photograph of a modern remodeled kitchen with white cabinets and dark stone counters">
  <div class="abs hero-frame"></div>
  <div class="abs hero-copy">
    <div class="hero-title">QUEN BRICKHALL</div>
    <div class="hero-sub">HIGH END CONSTRUCTION / REMODELING</div>
    <p class="hero-text">Lorem ipsum dolor sit amet, consectetur adipiscing elit, sed do eiu smod tempor incididunt ut labore et dolore magna aliqua.t enimad minim veniant ut labore et dm.</p>
  </div>
  <div class="abs hero-dots"><span></span><span></span><span></span><span class="on"></span></div>
  <svg class="abs arrow" style="left:18px" width="16" height="32" viewBox="0 0 16 32"><path d="M15 1 1 16l14 15" fill="none" stroke="#fff" stroke-width="1.2"/></svg>
  <svg class="abs arrow" style="left:660px" width="16" height="32" viewBox="0 0 16 32"><path d="M1 1l14 15L1 31" fill="none" stroke="#fff" stroke-width="1.2"/></svg>
</section>

<section class="section features">
  <div class="abs feature" style="left:94px">
    <svg width="40" height="36" viewBox="0 0 40 36"><circle cx="17" cy="17" r="14" fill="none" stroke="#ff6a00" stroke-width="2.4"/><path d="M17 8v9l-5 4" fill="none" stroke="#ff6a00" stroke-width="2.2"/><path d="M24 27c2-3 5-3 6 0s4 3 6 0-4-3-6 0-4 3-6 0z" fill="none" stroke="#ff6a00" stroke-width="2"/></svg>
    <h3>End to End Solution</h3>
    <p>At vero eos et accusamus et iustod io dignissimos ducimus qui bl ditii praesentium voluptatum.</p>
    <div class="more">READ MORE &#8853;</div>
  </div>
  <div class="abs feature" style="left:277px">
    <svg width="40" height="36" viewBox="0 0 40 36"><rect x="4" y="4" width="28" height="28" fill="#ff6a00"/></svg>
    <h3>Remodeling</h3>
    <p>At vero eos et accusamus et iustod io dignissimos ducimus qui bl ditii praesentium voluptatum.</p>
    <div class="more">READ MORE &#8853;</div>
  </div>
  <div class="abs feature" style="left:454px">
    <svg width="40" height="36" viewBox="0 0 40 36"><path d="M2 16h7v17H2zM11 16l7-13c3 0 4 2 3 6l-1 5h10c2 0 3 2 2 4l-4 13c-.5 1.5-1.5 2-3 2H11z" fill="none" stroke="#ff6a00" stroke-width="2.4" stroke-linejoin="round"/></svg>
    <h3>High Quality Standards</h3>
    <p>At vero eos et accusamus et iustod io dignissimos ducimus qui bl ditii praesentium voluptatum.</p>
    <div class="more">READ MORE &#8853;</div>
  </div>
</section>

<section class="section gallery">
  <h2 class="abs section-title">OUR PHOTO <em>GALLERY</em></h2>
  <div class="abs filters">
    <span class="active">All</span><span>Kitchens</span><span>Bathrooms</span><span>Additions</span><span>Living Room</span><span>Basements</span><span>Laundry/Mud Room</span><span>Outdoor Living</span>
  </div>
  <div class="abs thumb" style="left:94px;background:linear-gradient(160deg,#7a4a2a,#b07a4a 50%,#3a2a22)" role="img" aria-label="Photo of a kitchen range with tiled backsplash"></div>
  <div class="abs thumb" style="left:225px;background:linear-gradient(160deg,#8e8a80,#cfc6b6 55%,#6e6a62)" role="img" aria-label="Photo of a stone-clad bathtub"></div>
  <div class="abs thumb" style="left:356px;background:linear-gradient(160deg,#9aa3a0,#d6dad6 55%,#7f8784)" role="img" aria-label="Photo of a tiled walk-in shower"></div>
  <div class="abs thumb" style="left:486px;background:linear-gradient(160deg,#c9bfb4,#8d7866 55%,#4a3a30)" role="img" aria-label="Photo of a bright kitchen with pale cabinets"></div>
  <div class="abs dots"><span></span><span></span><span></span><span class="on"></span><span></span><span></span><span></span></div>
</section>

<section class="section about">
  <h2 class="abs about-title">ABOUT QUEN<span>BRICKHALL REMODELING</span></h2>
  <p class="abs about-text">At vero eos et accusamus et iusto odio dignissimos ducimus qui blan ditiis praesentium voluptatum deleniti atque corrupti quos dolores et quas molestias excepturi sint occaecati cupiditate non provident, simi lique sunt in culpa qui officia deserunt mollitia animi, id est laborum et dolorum fuga. Et harum quidem rerum facilis est et expedita disti nc am libero tempore, cum soluta nobis est eligendi optio cum.</p>
  <div class="abs btn">READ MORE <span>&#8853;</span></div>
  <div class="abs about-photo" style="left:316px;background:linear-gradient(180deg,#b9c2c8,#c7a070 60%,#2b2b2b)" role="img" aria-label="Photo of a kitchen with a window overlooking the city"></div>
  <div class="abs about-photo" style="left:465px;background:linear-gradient(180deg,#d9d2c4,#a69a86 55%,#2c2a28)" role="img" aria-label="Photo of a room with shoji screens and a dark stone counter"></div>
</section>

<section class="section testimonials">
  <h2 class="abs section-title">CLIENT <em>TESTIMONIALS</em></h2>
  <div class="abs avatar" role="img" aria-label="Portrait of the client"></div>
  <div class="abs quote-badge">&#8220;</div>
  <p class="abs quote"><b>&#8220;</b> At vero eos et accusamus et iusto odio dignissimos ducimus qui blanditiis praesentium voluptatum deleniti atque corrupti quos dolores et quas mol estias excepturi sint occaecati cupiditate non provident, similique sunt in culpa qui officia deserunt mollitia animi, id est laborum et dolorum fuga. Et harum quidem rerum facilis est et expedita distinctio. Nam libero tempore, cum soluta nobis est eligendi optio cumque nihil impedit quo minus id quod maxime placeat facere uidem rerum facilis est et expedita distinctioam libero <b>&#8221;</b></p>
  <div class="abs author">JHO SMITH, CITY NAME</div>
</section>

<footer class="section site-footer">
  <div class="abs footer-brand">
    <div class="brand-mark"></div>
    <div class="brand-name">QUEN BRICKHALL<br>REMODELING</div>
  </div>
  <div class="abs footer-head" style="left:252px">LINKS</div>
  <div class="abs links">HOME<br>ABOUT<br>CONTACT US<br>WHAT WE DO<br>SERVICES<br>GALLERY</div>
  <div class="abs footer-head" style="left:354px">CONTACT US</div>
  <div class="abs contact">
    <div class="row"><span class="ico">&#9873;</span><span>Mailing Address: 2280 Alder Ct<br>94025 Menlo Park,CA</span></div>
    <div class="row"><span class="ico">&#9646;</span><span>Phone: 650-555-0193</span></div>
    <div class="row"><span class="ico">&#9993;</span><span>Email: info@quenbrickhall.com</span></div>
  </div>
  <div class="abs socials"><span></span><span></span><span></span><span></span></div>
  <div class="abs footer-head" style="left:503px">CONTACT FORM</div>
  <div class="abs field" style="top:42px">Name:</div>
  <div class="abs field" style="top:59px">Email:</div>
  <div class="abs field" style="top:76px;height:21px">Short Message:</div>
  <div class="abs submit">SUBMIT</div>
</footer>

<div class="section bottom-bar">
  <div class="abs legal">PRIVACY POLICY &nbsp;| &nbsp;TERMS AND CONDITIONS | &nbsp;SITEMAP</div>
  <div class="abs copyright">Copyright &copy; 2016 &nbsp;All Rights Reserved.quenbrickhall.com</div>
  <div class="abs tag">C4</div>
</div>

</body>
</html>
```